Real Estate Virtual 360 Tour Web Home Page [Design Only]

see new upload mockup attached

We want new design ideas for our home page.

Link to video from web dev team of wireframe for reference: https://files.quorvantshare.net/d/7q-WpR2n8Lx4Tb6Hc0Yv9Ke3Mz5Ud/view?usp=sharing

Things desired on the home page:

Book a shoot now - Multiple markets,links to the corresponding market page for actual booking

1 Complete Package - includes Video, 3D Doviquell Tours, Exterior 360 Tours, Map, Agent Profile, Floor Plans, 2D Photos with blue sky and twilight sky guarantee

How it Works-https://clipnestra.net/582716049

Pricing-https://brisklumehomes.net/pricing/

House Search-https://brisklumehomes.net/

Footer
Updates

Target Market(s)

Real Estate Agents, Realtors, Home Buyers

Number of Pages Required

1 page

Font styles to use
Sans Serif

Colors
0555a3

Requirements
Must have
• see new upload mockup attached

Footer

```html
<!DOCTYPE html>
<html lang="en">
<head>
<meta charset="utf-8">
<title>Brisklume Homes – Virtual 360 Tours</title>
<link rel="stylesheet" href="https://fonts.googleapis.com/css2?family=Open+Sans:wght@400;600;700;800&display=swap">
<style>
:root{
  --blue:#0555a3;
  --blue-dark:#033d78;
  --blue-soft:#e6f0fa;
  --blue-tint:#d3e4f5;
  --ink:#1f2a37;
  --muted:#6b7785;
  --line:#d9e1ea;
  --page:#ffffff;
  --bg:#eef2f6;
  --gold:#f5b400;
  --map:#dde4dc;
}
*{box-sizing:border-box;margin:0;padding:0}
html,body{width:706px;height:1200px;overflow:hidden}
body{background:var(--bg);font-family:"Open Sans",Arial,sans-serif;color:var(--ink);font-size:6px;line-height:1.35;position:relative}
.col{position:absolute;background:var(--page);box-shadow:0 0 4px rgba(0,0,0,.08);overflow:hidden}
.col-left{left:10px;top:8px;width:344px;height:1184px}
.col-right{left:362px;top:8px;width:336px;height:350px}
.btn{display:inline-block;background:var(--blue);color:#fff;font-weight:600;font-size:6px;padding:4px 9px;border-radius:2px;border:1px solid var(--blue);white-space:nowrap}
.btn-outline{background:#fff;color:var(--blue)}
.section-title{font-size:12px;font-weight:700;color:var(--blue);text-align:center}
.section-title::after{content:"";display:block;width:26px;height:2px;background:var(--blue);margin:3px auto 0}
.ph{display:block}

/* header */
.site-header{height:36px;display:flex;align-items:center;justify-content:space-between;gap:6px;padding:0 10px;border-bottom:1px solid var(--line)}
.brand{display:flex;align-items:center;gap:4px;font-weight:800;font-size:7px;color:var(--blue);line-height:1;white-space:nowrap}
.brand-mark{width:10px;height:10px;background:var(--blue)}
.main-nav{display:flex;gap:6px;font-size:5px;color:var(--ink);white-space:nowrap}
.header-cta{display:flex;align-items:center;gap:5px;font-size:5px;color:var(--blue);font-weight:600;white-space:nowrap}

/* hero */
.hero{display:flex;height:126px}
.hero-photo{width:185px;height:100%;background:linear-gradient(180deg,#9ec4e6 0%,#cfd9e3 35%,#c9b7a0 70%,#8f7c68 100%)}
.hero-copy{flex:1;background:var(--blue-soft);display:flex;flex-direction:column;justify-content:center;align-items:center;padding:0 8px;text-align:center}
.hero-copy h1{font-size:12px;line-height:1.25;font-weight:800;color:var(--blue);margin-bottom:9px;white-space:nowrap}
.hero-actions{display:flex;gap:5px}

/* package */
.package{display:flex;padding:10px;gap:10px;height:170px}
.package-info{width:140px}
.package-info h2{font-size:7.5px;font-weight:700;color:var(--blue);margin-bottom:5px;line-height:1.3}
.checklist{list-style:none;margin-bottom:8px}
.checklist li{display:flex;align-items:center;gap:4px;font-size:5.5px;margin-bottom:3px}
.checklist svg{width:6px;height:6px;flex:none}
.package-actions{display:flex;gap:4px}
.feature-grid{flex:1;display:grid;grid-template-columns:repeat(3,1fr);gap:5px}
.feature{background:var(--blue-soft);border:1px solid var(--blue-tint);border-radius:3px;display:flex;flex-direction:column;align-items:center;justify-content:center;gap:4px;font-size:5.5px;font-weight:600;color:var(--blue);text-align:center}
.feature svg{width:16px;height:16px}
.feature.is-active{background:var(--blue);color:#fff;border-color:var(--blue)}

/* how it works */
.how{display:flex;gap:10px;padding:0 10px;height:96px}
.how-banner{width:140px;background:linear-gradient(160deg,#3b4652,#6d7b88);display:flex;align-items:center;justify-content:center;text-align:center;padding:8px}
.how-banner p{color:#fff;font-weight:800;font-size:9px;line-height:1.2}
.how-steps{flex:1}
.how-steps .section-title{font-size:10px;margin-bottom:5px}
.steps{list-style:none}
.steps li{display:flex;align-items:center;gap:4px;font-size:5.5px;margin-bottom:3px}
.steps b{width:8px;height:8px;border-radius:50%;background:var(--blue);color:#fff;font-size:5px;display:flex;align-items:center;justify-content:center;flex:none}
.how-actions{display:flex;gap:4px;justify-content:center;margin-top:4px}

/* search */
.search{padding:12px 10px 0}
.search .section-title{margin-bottom:7px}
.search-box{border:1px solid var(--line);border-radius:3px;padding:8px;box-shadow:0 1px 3px rgba(0,0,0,.06)}
.field-row{display:flex;gap:6px;margin-bottom:6px}
.field{flex:1;height:12px;border:1px solid var(--line);border-radius:2px;font-size:5.5px;color:var(--muted);display:flex;align-items:center;justify-content:space-between;padding:0 4px}
.range{flex:1;font-size:5px;color:var(--muted)}
.range-track{height:2px;background:var(--line);margin-top:3px;position:relative}
.range-track i{position:absolute;left:20%;right:30%;top:0;bottom:0;background:var(--blue)}
.checks{display:flex;gap:14px;font-size:5.5px;color:var(--muted);margin-bottom:6px;justify-content:center}
.checks span::before{content:"";display:inline-block;width:5px;height:5px;border:1px solid var(--muted);margin-right:3px;vertical-align:-1px}
.search-submit{text-align:center}

/* listings */
.listings{display:grid;grid-template-columns:repeat(3,1fr);gap:10px 8px;padding:12px 10px 0}
.listing{border:1px solid var(--line);border-radius:3px;overflow:hidden;height:132px}
.listing-photo{height:62px;background:linear-gradient(180deg,#a9cbe8 0%,#c8d4de 45%,#8e9a7e 100%)}
.listing-body{padding:5px}
.listing-address{font-size:5.5px;font-weight:600;margin-bottom:4px;min-height:16px}
.listing-meta{display:flex;justify-content:space-between;font-size:5px;color:var(--muted);margin-bottom:4px}
.listing-price{font-size:7px;font-weight:700;color:var(--blue);margin-bottom:5px}
.listing .btn{display:block;text-align:center}

.pager{display:flex;justify-content:center;gap:4px;padding:8px 0}
.pager span{width:10px;height:10px;border-radius:50%;border:1px solid var(--blue);color:var(--blue);font-size:5px;display:flex;align-items:center;justify-content:center}
.pager span.is-current{background:var(--blue);color:#fff}

.map{margin:0 10px;height:92px;background:var(--map)}

/* pricing */
.pricing{padding:12px 10px 0}
.pricing .section-title{margin-bottom:8px}
.pricing-layout{display:flex;gap:8px}
.pricing-menu{width:88px;background:var(--bg);list-style:none;padding:5px 0}
.pricing-menu li{font-size:5.5px;padding:4px 6px;border-bottom:1px solid var(--line)}
.pricing-menu li.is-active{background:var(--blue);color:#fff;font-weight:600}
.tiers{flex:1}
.tier{display:flex;align-items:center;gap:6px;border:1px solid var(--line);border-radius:2px;margin-bottom:3px;padding-right:6px}
.tier-badge{width:18px;height:16px;background:var(--blue);color:#fff;font-size:4.5px;font-weight:700;display:flex;align-items:center;justify-content:center;flex:none}
.tier-name{flex:1;font-size:5.5px;font-weight:600;white-space:nowrap}
.tier svg{width:6px;height:6px}
.tier-detail{font-size:5px;color:var(--muted);padding:0 0 4px 24px}
.tier-detail .btn{margin-top:3px}

/* testimonials */
.testimonials{padding:8px 10px 0}
.testimonials .section-title{margin-bottom:8px}
.reviews{display:flex;gap:8px}
.review{flex:1;border:1px solid var(--line);border-radius:3px;padding:6px;text-align:center;box-shadow:0 1px 3px rgba(0,0,0,.06)}
.avatar{width:20px;height:20px;border-radius:50%;background:linear-gradient(135deg,#b7c6d6,#8597aa);margin:0 auto 3px}
.review h3{font-size:6px;font-weight:700}
.stars{color:var(--gold);font-size:6px;letter-spacing:1px;margin:1px 0 2px}
.review p{font-size:5px;color:var(--muted)}
.dots{display:flex;justify-content:center;align-items:center;gap:3px;margin-top:6px}
.dots i{width:4px;height:4px;border-radius:50%;background:var(--line)}
.dots i.is-current{background:var(--blue)}
.dots b{width:7px;height:7px;background:var(--blue);color:#fff;font-size:5px;display:flex;align-items:center;justify-content:center}

/* team */
.team{display:flex;gap:8px;padding:20px 10px 0}
.team-copy{width:110px}
.team-copy h2{font-size:11px;font-weight:700;color:var(--blue)}
.team-copy h2::after{content:"";display:block;width:22px;height:2px;background:var(--blue);margin:3px 0 5px}
.team-copy p{font-size:5px;color:var(--muted);margin-bottom:6px}
.team-grid{flex:1;display:grid;grid-template-columns:repeat(3,1fr);gap:4px}
.team-photo{height:56px;background:linear-gradient(180deg,#d7dde4,#9aa7b5)}

/* footer */
.site-footer{position:absolute;left:0;right:0;bottom:0;height:78px}
.footer-cols{display:flex;gap:10px;padding:6px 10px;height:66px}
.footer-col{flex:1}
.footer-col h4{font-size:6px;font-weight:700;color:var(--blue);margin-bottom:3px}
.footer-col li{list-style:none;font-size:5px;color:var(--muted);margin-bottom:2px;display:flex;gap:3px;align-items:center}
.footer-col li svg{width:5px;height:5px}
.mini-input{height:9px;border:1px solid var(--line);border-radius:1px;margin-bottom:3px;font-size:5px;color:var(--muted);padding:1px 3px}
.socials{display:flex;gap:3px;margin-top:3px}
.socials i{width:7px;height:7px;background:var(--blue)}
.footer-bar{height:12px;background:var(--blue);color:#fff;font-size:5px;display:flex;align-items:center;justify-content:center}
</style>
</head>
<body>

<main class="col col-left">
  <header class="site-header">
    <div class="brand"><span class="brand-mark"></span>BRISKLUME HOMES</div>
    <nav class="main-nav"><span>Home</span><span>About</span><span>Packages</span><span>Pricing</span><span>Book a Shoot</span><span>Contact</span></nav>
    <div class="header-cta"><span>(555) 014-2290</span><span class="btn">Book Now</span></div>
  </header>

  <section class="hero">
    <div class="hero-photo ph" role="img" aria-label="Photo of a white multi-storey residential building against a blue sky"></div>
    <div class="hero-copy">
      <h1>See Your Next Home<br>From Every Angle</h1>
      <div class="hero-actions"><span class="btn">View Packages</span><span class="btn btn-outline">Book a Shoot</span></div>
    </div>
  </section>

  <section class="package">
    <div class="package-info">
      <h2>All Brisklume Homes' New One Complete Package Includes:</h2>
      <ul class="checklist">
        <li><svg viewBox="0 0 10 10"><circle cx="5" cy="5" r="5" fill="#0555a3"/><path d="M2.5 5.2l1.7 1.7 3.4-3.6" stroke="#fff" stroke-width="1.3" fill="none"/></svg>Video Tour</li>
        <li><svg viewBox="0 0 10 10"><circle cx="5" cy="5" r="5" fill="#0555a3"/><path d="M2.5 5.2l1.7 1.7 3.4-3.6" stroke="#fff" stroke-width="1.3" fill="none"/></svg>3D Doviquell Tours</li>
        <li><svg viewBox="0 0 10 10"><circle cx="5" cy="5" r="5" fill="#0555a3"/><path d="M2.5 5.2l1.7 1.7 3.4-3.6" stroke="#fff" stroke-width="1.3" fill="none"/></svg>Exterior 360 Tours</li>
        <li><svg viewBox="0 0 10 10"><circle cx="5" cy="5" r="5" fill="#0555a3"/><path d="M2.5 5.2l1.7 1.7 3.4-3.6" stroke="#fff" stroke-width="1.3" fill="none"/></svg>Neighborhood Map</li>
        <li><svg viewBox="0 0 10 10"><circle cx="5" cy="5" r="5" fill="#0555a3"/><path d="M2.5 5.2l1.7 1.7 3.4-3.6" stroke="#fff" stroke-width="1.3" fill="none"/></svg>Agent Profile</li>
        <li><svg viewBox="0 0 10 10"><circle cx="5" cy="5" r="5" fill="#0555a3"/><path d="M2.5 5.2l1.7 1.7 3.4-3.6" stroke="#fff" stroke-width="1.3" fill="none"/></svg>Floor Plans</li>
        <li><svg viewBox="0 0 10 10"><circle cx="5" cy="5" r="5" fill="#0555a3"/><path d="M2.5 5.2l1.7 1.7 3.4-3.6" stroke="#fff" stroke-width="1.3" fill="none"/></svg>2D Photos</li>
        <li><svg viewBox="0 0 10 10"><circle cx="5" cy="5" r="5" fill="#0555a3"/><path d="M2.5 5.2l1.7 1.7 3.4-3.6" stroke="#fff" stroke-width="1.3" fill="none"/></svg>Blue Sky Guarantee</li>
        <li><svg viewBox="0 0 10 10"><circle cx="5" cy="5" r="5" fill="#0555a3"/><path d="M2.5 5.2l1.7 1.7 3.4-3.6" stroke="#fff" stroke-width="1.3" fill="none"/></svg>Twilight Sky Guarantee</li>
      </ul>
      <div class="package-actions"><span class="btn">View Pricing</span><span class="btn btn-outline">Book a Shoot</span></div>
    </div>
    <div class="feature-grid">
      <div class="feature"><svg viewBox="0 0 20 20" fill="none" stroke="currentColor" stroke-width="1.4"><rect x="2" y="5" width="12" height="10" rx="1"/><path d="M14 9l4-2v6l-4-2"/></svg>Video Tour</div>
      <div class="feature"><svg viewBox="0 0 20 20" fill="none" stroke="currentColor" stroke-width="1.4"><path d="M10 2l7 4v8l-7 4-7-4V6z"/><path d="M3 6l7 4 7-4M10 10v8"/></svg>3D Tours</div>
      <div class="feature"><svg viewBox="0 0 20 20" fill="none" stroke="currentColor" stroke-width="1.4"><ellipse cx="10" cy="10" rx="8" ry="4"/><path d="M3 8l7-5 7 5v6H3z"/></svg>Exterior 360</div>
      <div class="feature"><svg viewBox="0 0 20 20" fill="none" stroke="currentColor" stroke-width="1.4"><path d="M10 18s6-6 6-10a6 6 0 0 0-12 0c0 4 6 10 6 10z"/><circle cx="10" cy="8" r="2"/></svg>Map</div>
      <div class="feature is-active"><svg viewBox="0 0 20 20" fill="none" stroke="currentColor" stroke-width="1.4"><circle cx="10" cy="7" r="3.5"/><path d="M3 18c1-4 4-6 7-6s6 2 7 6"/></svg>Agent Profile</div>
      <div class="feature"><svg viewBox="0 0 20 20" fill="none" stroke="currentColor" stroke-width="1.4"><rect x="2" y="2" width="16" height="16"/><path d="M2 10h8v8M10 2v5M14 10h4"/></svg>Floor Plans</div>
      <div class="feature"><svg viewBox="0 0 20 20" fill="none" stroke="currentColor" stroke-width="1.4"><rect x="2" y="5" width="16" height="12" rx="1"/><circle cx="10" cy="11" r="3"/><path d="M7 5l1-2h4l1 2"/></svg>2D Photos</div>
      <div class="feature"><svg viewBox="0 0 20 20" fill="none" stroke="currentColor" stroke-width="1.4"><circle cx="10" cy="10" r="4"/><path d="M10 1v3M10 16v3M1 10h3M16 10h3M4 4l2 2M14 14l2 2M4 16l2-2M14 6l2-2"/></svg>Blue Sky</div>
      <div class="feature"><svg viewBox="0 0 20 20" fill="none" stroke="currentColor" stroke-width="1.4"><path d="M15 13A7 7 0 0 1 7 3a7 7 0 1 0 8 10z"/></svg>Twilight Sky</div>
    </div>
  </section>

  <section class="how">
    <div class="how-banner ph" role="img" aria-label="Photo of a home exterior with overlaid headline"><p>ONE COMPLETE PACKAGE AT ONE LOW PRICE</p></div>
    <div class="how-steps">
      <h2 class="section-title">How It Works</h2>
      <ol class="steps">
        <li><b>1</b>Choose your market and pick a shoot date.</li>
        <li><b>2</b>Our photographer captures every room in 360.</li>
        <li><b>3</b>We edit photos, video and floor plans.</li>
        <li><b>4</b>Your tour link is delivered within 24 hours.</li>
        <li><b>5</b>Share the listing and welcome more buyers.</li>
      </ol>
      <div class="how-actions"><span class="btn">View Packages</span><span class="btn btn-outline">Book a Shoot</span></div>
    </div>
  </section>

  <section class="search">
    <h2 class="section-title">Search Home</h2>
    <div class="search-box">
      <div class="field-row">
        <div class="field">City or ZIP<span>▾</span></div>
        <div class="field">Property Type<span>▾</span></div>
        <div class="field">Any Price<span>▾</span></div>
      </div>
      <div class="field-row">
        <div class="range">Bedrooms<div class="range-track"><i></i></div></div>
        <div class="range">Bathrooms<div class="range-track"><i></i></div></div>
        <div class="range">Square Feet<div class="range-track"><i></i></div></div>
      </div>
      <div class="checks"><span>Garage</span><span>Pool</span><span>Open House</span><span>New Listing</span></div>
      <div class="search-submit"><span class="btn">Search</span></div>
    </div>
  </section>

  <section class="listings">
    <article class="listing"><div class="listing-photo ph" role="img" aria-label="Photo of a two-storey house"></div><div class="listing-body"><p class="listing-address">1425 Maple Grove Avenue, Lakeview</p><div class="listing-meta"><span>4 Beds</span><span>3 Baths</span></div><p class="listing-price">$ 1,245,000</p><span class="btn">View Details</span></div></article>
    <article class="listing"><div class="listing-photo ph" role="img" aria-label="Photo of a family house with lawn"></div><div class="listing-body"><p class="listing-address">88 Cedar Hill Road, Brookfield</p><div class="listing-meta"><span>3 Beds</span><span>2 Baths</span></div><p class="listing-price">$ 689,000</p><span class="btn">View Details</span></div></article>
    <article class="listing"><div class="listing-photo ph" role="img" aria-label="Photo of a brick house"></div><div class="listing-body"><p class="listing-address">302 Willow Lane, Riverbend</p><div class="listing-meta"><span>5 Beds</span><span>4 Baths</span></div><p class="listing-price">$ 915,500</p><span class="btn">View Details</span></div></article>
    <article class="listing"><div class="listing-photo ph" role="img" aria-label="Photo of a suburban house"></div><div class="listing-body"><p class="listing-address">4810 Aspen Court, Fairmont</p><div class="listing-meta"><span>3 Beds</span><span>2 Baths</span></div><p class="listing-price">$ 549,900</p><span class="btn">View Details</span></div></article>
    <article class="listing"><div class="listing-photo ph" role="img" aria-label="Photo of a modern home"></div><div class="listing-body"><p class="listing-address">17 Harbor View Drive, Seaside</p><div class="listing-meta"><span>4 Beds</span><span>3 Baths</span></div><p class="listing-price">$ 1,080,000</p><span class="btn">View Details</span></div></article>
    <article class="listing"><div class="listing-photo ph" role="img" aria-label="Photo of a colonial style house"></div><div class="listing-body"><p class="listing-address">960 Oak Ridge Street, Millbrook</p><div class="listing-meta"><span>4 Beds</span><span>2 Baths</span></div><p class="listing-price">$ 734,000</p><span class="btn">View Details</span></div></article>
  </section>

  <div class="pager"><span>‹</span><span class="is-current">1</span><span>2</span><span>3</span><span>›</span></div>

  <div class="map ph" role="img" aria-label="Map showing the locations of listed homes"></div>

  <section class="pricing">
    <h2 class="section-title">Pricing and Online Scheduling</h2>
    <div class="pricing-layout">
      <ul class="pricing-menu">
        <li>Select Your Market</li>
        <li class="is-active">Northern County Area</li>
        <li>Metro Downtown</li>
        <li>Coastal Region</li>
        <li>Lake District</li>
        <li>Valley &amp; Foothills</li>
        <li>Other Markets</li>
      </ul>
      <div class="tiers">
        <div class="tier"><span class="tier-badge">TIER 1</span><span class="tier-name">0 – 1,500 Sq Ft Complete Package</span><svg viewBox="0 0 6 6"><path d="M1 2l2 2 2-2" stroke="#0555a3" fill="none"/></svg></div>
        <div class="tier"><span class="tier-badge">TIER 2</span><span class="tier-name">1,501 – 2,500 Sq Ft Complete Package</span><svg viewBox="0 0 6 6"><path d="M1 2l2 2 2-2" stroke="#0555a3" fill="none"/></svg></div>
        <div class="tier"><span class="tier-badge">TIER 3</span><span class="tier-name">2,501 – 3,500 Sq Ft Complete Package</span><svg viewBox="0 0 6 6"><path d="M1 4l2-2 2 2" stroke="#0555a3" fill="none"/></svg></div>
        <div class="tier-detail">Includes video, 3D tour, exterior 360, floor plans and photos.<br><span class="btn">Book a Shoot</span></div>
        <div class="tier"><span class="tier-badge">TIER 4</span><span class="tier-name">3,501 – 4,500 Sq Ft Complete Package</span><svg viewBox="0 0 6 6"><path d="M1 2l2 2 2-2" stroke="#0555a3" fill="none"/></svg></div>
        <div class="tier"><span class="tier-badge">TIER 5</span><span class="tier-name">4,501 – 6,000 Sq Ft Complete Package</span><svg viewBox="0 0 6 6"><path d="M1 2l2 2 2-2" stroke="#0555a3" fill="none"/></svg></div>
        <div class="tier"><span class="tier-badge">TIER 6</span><span class="tier-name">6,001+ Sq Ft Complete Package</span><svg viewBox="0 0 6 6"><path d="M1 2l2 2 2-2" stroke="#0555a3" fill="none"/></svg></div>
      </div>
    </div>
  </section>
</main>

<aside class="col col-right">
  <section class="testimonials">
    <h2 class="section-title">Testimonial</h2>
    <div class="reviews">
      <div class="review"><div class="avatar" role="img" aria-label="Client portrait"></div><h3>Laura Benton</h3><div class="stars">★★★★★</div><p>The 360 tour brought twice the showings. Fast, friendly and very professional crew.</p></div>
      <div class="review"><div class="avatar" role="img" aria-label="Client portrait"></div><h3>Marcus Hale</h3><div class="stars">★★★★★</div><p>One package covered everything I needed. Buyers loved walking the home online.</p></div>
      <div class="review"><div class="avatar" role="img" aria-label="Client portrait"></div><h3>Priya Sandoval</h3><div class="stars">★★★★★</div><p>Booking was simple and the twilight photos made my listing stand out.</p></div>
    </div>
    <div class="dots"><b>‹</b><i class="is-current"></i><i></i><i></i><b>›</b></div>
  </section>

  <section class="team">
    <div class="team-copy">
      <h2>Our Team</h2>
      <p>Our photographers and editors are real estate specialists who capture every home with care. From the first booking to the final tour link, we help agents present listings that buyers can explore from anywhere, at any time.</p>
      <span class="btn">Meet the Team</span>
    </div>
    <div class="team-grid">
      <div class="team-photo ph" role="img" aria-label="Team member portrait"></div>
      <div class="team-photo ph" role="img" aria-label="Team member portrait"></div>
      <div class="team-photo ph" role="img" aria-label="Team member portrait"></div>
      <div class="team-photo ph" role="img" aria-label="Team member portrait"></div>
      <div class="team-photo ph" role="img" aria-label="Team member portrait"></div>
      <div class="team-photo ph" role="img" aria-label="Team member portrait"></div>
    </div>
  </section>

  <footer class="site-footer">
    <div class="footer-cols">
      <div class="footer-col">
        <h4>Contact Us</h4>
        <ul>
          <li><svg viewBox="0 0 6 6"><path d="M1 0.5l1.2 0 .6 1.5-.8.6a3 3 0 0 0 1.4 1.4l.6-.8 1.5.6V5A.5.5 0 0 1 5 5.5 4.5 4.5 0 0 1 .5 1 .5.5 0 0 1 1 .5z" fill="#0555a3"/></svg>(555) 014-2290</li>
          <li><svg viewBox="0 0 6 6"><rect x=".5" y="1" width="5" height="4" fill="none" stroke="#0555a3" stroke-width=".8"/><path d="M.5 1l2.5 2 2.5-2" stroke="#0555a3" fill="none" stroke-width=".8"/></svg>hello@brisklumehomes.net</li>
          <li><svg viewBox="0 0 6 6"><path d="M3 6S1 3.5 1 2.2a2 2 0 0 1 4 0C5 3.5 3 6 3 6z" fill="#0555a3"/></svg>210 Harborline Blvd, Suite 4</li>
        </ul>
        <div class="socials"><i></i><i></i><i></i><i></i></div>
      </div>
      <div class="footer-col">
        <h4>Stay Informed</h4>
        <div class="mini-input">Your Name</div>
        <div class="mini-input">Email Address</div>
        <span class="btn">Subscribe</span>
      </div>
      <div class="footer-col">
        <h4>Quick Links</h4>
        <ul>
          <li>Home</li><li>Packages</li><li>Pricing</li><li>Book a Shoot</li><li>Search Homes</li>
        </ul>
      </div>
    </div>
    <div class="footer-bar">© 2024 Brisklume Homes. All rights reserved.</div>
  </footer>
</aside>

</body>
</html>
```